Gutschein für Fotograf
Designer PelaWix hat meinen Geschmack am besten getroffen, ging auf meine Änderungsvorschläge genau ein, und änderte Details zu meiner vollsten Zufriedenheit. Kann ich auf alle Fälle weiter empfehlen.
Zielgruppe
Ich bin Fotograf und suche nach einem Gutschein für meine Arbeiten. Zielgruppen sind Privatpersonen, Pärchenfotos, Hochzeit, Baby usw.
Aufgabenstellung
Der Gutschein sollte zu meiner Homepage passen und auch zu meinen Bildern/ meinem Stil.
Folgendes könnte darauf stehen: (Foto) Gutschein - einzulösen bei - meine Homepage sollte darauf sein - es sollte eine Version mit 50 € sein und eine mit 100€ geben. Mir gefällt wahrscheinlich etwas klassisches besser, aber auch retro/ vintage könnte ich mir gut vorstellen. Vor allem möchte ich aber, dass es weiblich/ feminin wirkt. Ob Bilder von mir auf dem Gutschein von Vorteil sind, kann ich leider nicht einschätzen, aber die Bilder können jederzeit von meiner Homepage zu Testzwecken verwendet werden.

```html
<!DOCTYPE html>
<html lang="de">
<head>
<meta charset="utf-8">
<title>Gutschein für ein Fotoshooting</title>
<link href="https://fonts.googleapis.com/css2?family=Poiret+One&family=Sacramento&display=swap" rel="stylesheet">
<style>
  :root {
    --page: #ffffff;
    --frame: #d9d7d5;
    --panel-light: #6a5c51;
    --panel-mid: #463b34;
    --panel-dark: #2b2421;
    --title: #b9b4b0;
    --text: #ece8e4;
    --field: rgba(200, 190, 182, 0.55);
    --field-text: #f3efec;
    --photo-border: #a78f7e;
  }
  * { margin: 0; padding: 0; box-sizing: border-box; }
  html, body {
    width: 1200px; height: 292px; overflow: hidden;
    background: var(--page);
    font-family: "Poiret One", sans-serif;
  }
  .spread {
    position: absolute; top: 16px; height: 264px;
    background: var(--frame);
    box-shadow: 2px 3px 4px rgba(0,0,0,0.35);
  }
  .spread--outside { left: 54px; width: 526px; }
  .spread--inside { left: 620px; width: 528px; }
  .panel {
    position: absolute; top: 6px; width: 253px; height: 252px;
    background: radial-gradient(ellipse at 50% 50%, var(--panel-light) 0%, var(--panel-mid) 45%, var(--panel-dark) 100%);
    overflow: hidden;
  }
  .spread--outside .panel--back { left: 5px; }
  .spread--outside .panel--front { left: 268px; }
  .spread--inside .panel--left { left: 4px; width: 254px; }
  .spread--inside .panel--right { left: 269px; }

  .title {
    position: absolute; left: 0; right: 0; top: 18px;
    text-align: center;
    font-family: "Sacramento", cursive;
    font-size: 60px; line-height: 1;
    color: var(--title);
    text-shadow: 1px 1px 2px rgba(0,0,0,0.5);
  }
  .subtitle {
    position: absolute; left: 0; right: 0; top: 73px;
    text-align: center; font-size: 12px; color: var(--text);
  }
  .photo {
    position: absolute;
    border: 2px solid var(--photo-border);
    border-radius: 4px;
    box-shadow: 1px 1px 3px rgba(0,0,0,0.6);
  }
  .photo--portrait { left: 17px; top: 99px; width: 71px; height: 90px; transform: rotate(-4deg);
    background: linear-gradient(160deg, #4a4566, #6b4a4a 55%, #2c2838); }
  .photo--wedding { left: 94px; top: 97px; width: 71px; height: 91px; transform: rotate(2deg);
    background: linear-gradient(170deg, #5e6f95, #c9b8a8 55%, #efeae6); }
  .photo--couple { left: 160px; top: 103px; width: 81px; height: 86px; transform: rotate(4deg);
    background: linear-gradient(160deg, #d3a22a, #8c6a2e 55%, #3b3330); }
  .contact {
    position: absolute; left: 0; right: 0; top: 198px;
    text-align: center; color: var(--text);
    font-size: 8.5px; line-height: 10.5px;
  }
  .contact .phone { font-size: 9.5px; }
  .sparkle { position: absolute; width: 26px; height: 26px; }
  .panel--front .sparkle { left: 5px; top: 175px; }
  .panel--right .sparkle { left: 205px; top: 18px; }

  .field {
    position: absolute; left: 34px; width: 185px; height: 21px;
    background: var(--field); border-radius: 6px;
    color: var(--field-text); font-size: 8px;
    padding: 6px 0 0 8px;
  }
  .field--recipient { top: 28px; }
  .field--value { top: 62px; }
  .field--signature { top: 94px; }
  .photographer {
    position: absolute; left: 34px; top: 130px; width: 98px; height: 98px;
    border-radius: 4px;
    background: radial-gradient(ellipse at 55% 45%, #c89f86 0%, #6b5246 35%, #141211 75%);
  }
  .services {
    position: absolute; left: 139px; top: 149px; width: 80px; height: 62px;
    background: var(--field); border-radius: 5px;
    color: var(--field-text); font-size: 8.5px; line-height: 10.5px;
    padding: 9px 0 0 9px;
  }
</style>
</head>
<body>
  <section class="spread spread--outside">
    <div class="panel panel--back"></div>
    <div class="panel panel--front">
      <h1 class="title">Gutschein</h1>
      <p class="subtitle">für ein Fotoshooting</p>
      <div class="photo photo--portrait" role="img" aria-label="Porträtfoto einer Frau mit langem Haar"></div>
      <div class="photo photo--wedding" role="img" aria-label="Hochzeitsfoto eines Brautpaares"></div>
      <div class="photo photo--couple" role="img" aria-label="Paarfoto vor herbstlichem Laub"></div>
      <svg class="sparkle" viewBox="0 0 26 26" aria-hidden="true">
        <path d="M13 0 L14 12 L26 13 L14 14 L13 26 L12 14 L0 13 L12 12 Z" fill="#fff" opacity="0.9"/>
        <circle cx="13" cy="13" r="2.5" fill="#fff"/>
      </svg>
      <p class="contact">bei Tobias Rakwitz<br>www.tobiasrakwitz.com<br><span class="phone">0660 5818204</span></p>
    </div>
  </section>

  <section class="spread spread--inside">
    <div class="panel panel--left"></div>
    <div class="panel panel--right">
      <div class="field field--recipient">Für</div>
      <div class="field field--value">Wert</div>
      <div class="field field--signature">Datum, Unterschrift</div>
      <svg class="sparkle" viewBox="0 0 26 26" aria-hidden="true">
        <path d="M13 0 L14 12 L26 13 L14 14 L13 26 L12 14 L0 13 L12 12 Z" fill="#fff" opacity="0.9"/>
        <circle cx="13" cy="13" r="2.5" fill="#fff"/>
      </svg>
      <div class="photographer" role="img" aria-label="Porträt des Fotografen mit Kamera vor dunklem Hintergrund"></div>
      <p class="services">People &amp; Portraits<br>Wedding<br>Couplefotos<br>und vieles mehr</p>
    </div>
  </section>
</body>
</html>
```